Letterhead

Can you please design me a letterhead that I can use electronically in word as a template. I have attached my business card as I would like the design to reflect this logo.

```html
<!DOCTYPE html>
<html lang="en">
<head>
<meta charset="utf-8">
<title>Calloway Business Consultants – Letterhead</title>
<link rel="stylesheet" href="https://fonts.googleapis.com/css2?family=Arimo:wght@400;700&family=Open+Sans:wght@400;600;700&display=swap">
<style>
  :root {
    --brand-red: #c8202e;
    --tint-pink: #f2c4c9;
    --faint-pink: #f1d6d9;
    --faint-grey: #c9c9c9;
    --ink: #333333;
    --paper: #ffffff;
  }
  html, body {
    margin: 0;
    padding: 0;
    overflow: hidden;
    background: var(--paper);
  }
  .letterhead {
    position: relative;
    width: 843px;
    height: 1200px;
    background: var(--paper);
    overflow: hidden;
    font-family: "Arimo", Arial, sans-serif;
  }
  .tint {
    position: absolute;
  }
  .tint--top {
    top: 0;
    left: 0;
    width: 843px;
    height: 180px;
    background: linear-gradient(180deg, rgba(242, 196, 201, 0.45) 0%, rgba(242, 196, 201, 0.18) 60%, rgba(242, 196, 201, 0) 100%);
  }
  .tint--bottom {
    bottom: 0;
    left: 300px;
    width: 543px;
    height: 170px;
    background: linear-gradient(160deg, rgba(242, 196, 201, 0) 35%, rgba(242, 196, 201, 0.5) 100%);
  }

  .brand {
    position: absolute;
    top: 22px;
    left: 545px;
  }
  .brand__name {
    margin: 0;
    font-size: 60px;
    font-weight: 400;
    line-height: 1;
    color: var(--brand-red);
  }
  .brand__tagline {
    margin: 6px 0 0 2px;
    font-size: 13px;
    line-height: 1.2;
    color: #111;
  }

  .footer-mark {
    position: absolute;
    left: 40px;
    top: 982px;
  }
  .footer-mark__name {
    margin: 0;
    font-size: 86px;
    line-height: 1;
    color: var(--faint-pink);
  }
  .footer-mark__tagline {
    margin: 4px 0 0 5px;
    font-size: 20px;
    line-height: 1.2;
    color: var(--faint-grey);
  }

  .contact {
    position: absolute;
    left: 35px;
    top: 1106px;
    font-family: "Open Sans", Arial, sans-serif;
    color: var(--ink);
  }
  .contact__person {
    margin: 0;
    font-size: 7.5px;
    line-height: 1.3;
    font-weight: 700;
  }
  .contact__role { color: var(--brand-red); font-weight: 600; }
  .contact__details {
    margin: 1px 0 0;
    font-size: 6.5px;
    line-height: 1.3;
  }
  .contact__label { color: var(--brand-red); font-weight: 700; }
  .sep { color: var(--brand-red); padding: 0 1px; }
</style>
</head>
<body>
  <main class="letterhead">
    <div class="tint tint--top" role="img" aria-label="Decorative fine-line wave pattern in soft red across the top of the page"></div>
    <div class="tint tint--bottom" role="img" aria-label="Decorative fine-line wave pattern in soft red at the bottom right corner"></div>

    <header class="brand">
      <h1 class="brand__name">calloway</h1>
      <p class="brand__tagline">Business Consultants Pty Ltd</p>
    </header>

    <section class="footer-mark" aria-hidden="true">
      <p class="footer-mark__name">calloway</p>
      <p class="footer-mark__tagline">Business Consultants Pty Ltd</p>
    </section>

    <footer class="contact">
      <p class="contact__person">Miriam Castell <span class="sep">|</span> <span class="contact__role">Principal</span></p>
      <p class="contact__details">
        <span class="contact__label">P</span> : 0412 555 018
        <span class="sep">|</span> <span class="contact__label">E</span> : miriam@calloway.net.au
        <span class="sep">|</span> <span class="contact__label">ACN</span> : 051 284 906
      </p>
    </footer>
  </main>
</body>
</html>
```